I want a business card that is going to show a creative spark but without limiting me to an industry. Something edgy but that wont go out of date. I want it state My business name Serafina Loire, profession - Professional Makeup Artist contact number and email

My service is to provide makeup services from bridal, fashion, photography, film, TV and so on. It is creative and different so i want that to be reflected.

I would like the card double sided.
Updates

 I would LOVE a background on my card something like this image... i can supply an image to be formed like this

Please use the image uploaded

Can we try using the image provided on one side of the card and then writing and details on the other side

Target Market(s)

I am targeting a wide range of people from Creative directors to the individual eg. bride

Industry/Entity Type

Business

Requirements
Must have
• Name: Delphine Hartwell
contact numbe 0417853120
email address:info@serafinaloire.com
website: www.serafinaloire.com
One of the images attached

professional makeup artist / hair stylist

I want it to show creativity
Nice to have
• logo, Double-sided card
Should not have
• the design should not use tradional style. Or images that are not my own

```html
<!DOCTYPE html>
<html lang="en">
<head>
<meta charset="utf-8">
<title>Serafina Loire — Business Card</title>
<link rel="stylesheet" href="https://fonts.googleapis.com/css2?family=Poiret+One&display=swap">
<style>
  :root {
    --stage-light: #a9a9a9;
    --stage-dark: #3c3c3c;
    --teal: #19c3cf;
    --teal-soft: #7fe3ea;
    --teal-deep: #137b80;
    --card-black: #020404;
    --paper-light: #f2f2f2;
    --paper-mid: #d3d3d3;
    --rule: #2cbfca;
    --eye-tones: #6f8a6e;
    --lip-tones: #b4504e;
  }
  * { margin: 0; padding: 0; box-sizing: border-box; }
  html, body { width: 931px; height: 1200px; overflow: hidden; }
  body {
    position: relative;
    font-family: "Poiret One", sans-serif;
    background: radial-gradient(ellipse at 50% 45%, var(--stage-light) 0%, #7b7b7b 55%, var(--stage-dark) 100%);
  }
  .side-label {
    position: absolute;
    left: 0; width: 100%;
    text-align: center;
    color: var(--teal);
    line-height: 1;
    letter-spacing: 2px;
  }
  .side-label--front { top: 0; font-size: 92px; }
  .side-label--back { top: 1085px; font-size: 112px; }

  .card {
    position: absolute;
    left: 11px; width: 897px;
    border-radius: 29px;
    overflow: hidden;
    box-shadow: 0 8px 18px rgba(0,0,0,.55);
  }
  .card--front {
    top: 98px; height: 467px;
    background: linear-gradient(90deg, var(--teal-deep) 0%, #0f6468 35%, #06292b 62%, var(--card-black) 85%);
  }
  .card--back {
    top: 621px; height: 464px;
    background: radial-gradient(ellipse at 40% 35%, var(--paper-light) 0%, #e3e3e3 50%, var(--paper-mid) 100%);
  }

  .artwork { position: absolute; border-radius: 40% 50% 40% 50%; }
  .artwork--front-eye {
    left: 10px; top: 89px; width: 310px; height: 245px;
    background: radial-gradient(ellipse at 45% 55%, rgba(120,150,90,.55) 0%, rgba(40,70,60,.45) 45%, rgba(20,80,80,0) 75%);
  }
  .artwork--back-eye {
    left: 161px; top: 26px; width: 244px; height: 165px;
    background: radial-gradient(ellipse at 50% 60%, rgba(140,200,110,.55) 0%, rgba(150,150,150,.35) 50%, rgba(200,200,200,0) 78%);
  }
  .artwork--lips {
    left: 10px; top: 350px; width: 173px; height: 86px;
    background: radial-gradient(ellipse at 45% 50%, rgba(180,80,78,.85) 0%, rgba(190,110,108,.5) 55%, rgba(220,200,200,0) 80%);
  }

  .brand-name, .brand-title, .contact { position: absolute; white-space: nowrap; }
  .card--front .brand-name {
    right: 17px; top: 180px;
    font-size: 72px; color: var(--teal-soft);
    text-shadow: 0 0 6px rgba(25,195,207,.6);
    letter-spacing: 2px;
  }
  .card--front .brand-title {
    right: 63px; top: 255px;
    font-size: 32px; color: var(--teal);
    text-shadow: 0 0 4px rgba(25,195,207,.5);
  }
  .card--back .brand-name {
    right: 22px; top: 100px;
    font-size: 60px; color: var(--teal);
    letter-spacing: 2px;
  }
  .card--back .brand-title {
    right: 60px; top: 160px;
    font-size: 28px; color: var(--teal);
  }
  .rule {
    position: absolute;
    left: 410px; right: 24px; top: 196px;
    height: 2px; background: var(--rule);
  }
  .contact-label {
    position: absolute;
    color: var(--teal);
    font-size: 33px;
    letter-spacing: 1px;
  }
  .contact-label--phone { left: 15px; top: 222px; }
  .contact-label--email { left: 58px; top: 300px; }
  .contact { color: var(--teal); }
  .contact--phone { left: 218px; top: 200px; font-size: 80px; letter-spacing: 4px; }
  .contact--email { left: 330px; top: 285px; font-size: 56px; line-height: 80px; letter-spacing: 2px; }
</style>
</head>
<body>
  <div class="side-label side-label--front">Front</div>

  <section class="card card--front">
    <div class="artwork artwork--front-eye" role="img" aria-label="Hand-sketched eye with teal and green eyeshadow"></div>
    <div class="brand-name">Serafina Loire</div>
    <div class="brand-title">Professional Makeup Artist</div>
  </section>

  <section class="card card--back">
    <div class="artwork artwork--back-eye" role="img" aria-label="Hand-sketched eye with green eyeshadow"></div>
    <div class="brand-name">Serafina Loire</div>
    <div class="brand-title">Professional Makeup Artist</div>
    <div class="rule"></div>
    <div class="contact-label contact-label--phone">Number&#9830;</div>
    <div class="contact contact--phone">0417&#8226;853&#8226;120</div>
    <div class="contact-label contact-label--email">E-mail&#9830;</div>
    <div class="contact contact--email">serafinaloire@<br>mailbox.com.au</div>
    <div class="artwork artwork--lips" role="img" aria-label="Hand-sketched red lips"></div>
  </section>

  <div class="side-label side-label--back">back</div>
</body>
</html>
```